Corvanth Consulting Card Design

Create a card design for the company.

Target Market(s)

B2B

Industry/Entity Type

Management Consulting

Contact Information for Business Card

Name; Role; email; phone; website;

Colors
0555a3
3276b5
85abd2
cee9f5

```html
<!DOCTYPE html>
<html lang="en">
<head>
<meta charset="UTF-8">
<title>Corvanth Consulting – Business Card</title>
<link rel="stylesheet" href="https://fonts.googleapis.com/css2?family=Ubuntu:wght@500;700&family=Open+Sans:wght@400;600;700&display=swap">
<style>
  :root {
    --stage: #000000;
    --navy: #0555a3;
    --blue: #3276b5;
    --sky: #85abd2;
    --ice: #cee9f5;
    --bright: #1a8ad4;
    --front-top: #03a3e3;
    --front-bottom: #0456ac;
    --ink: #454a50;
    --ink-soft: #8b9096;
    --band-grey: #8e9196;
    --paper: #ffffff;
  }
  * { margin: 0; padding: 0; box-sizing: border-box; }
  html, body {
    width: 1200px; height: 1000px; overflow: hidden;
    background: var(--stage);
  }
  .stage { position: relative; width: 1200px; height: 1000px; }

  .card { position: absolute; left: 286px; width: 628px; overflow: hidden; }

  /* Front */
  .card-front {
    top: 126px; height: 357px;
    background: radial-gradient(ellipse 120% 90% at 85% 0%, var(--front-top) 0%, #0a86d2 45%, var(--front-bottom) 100%);
  }
  .front-mark {
    position: absolute; left: 112px; top: 144px;
    width: 84px; height: 84px; border-radius: 50%;
    background: var(--paper);
  }
  .front-name {
    position: absolute; left: 242px; top: 142px;
    font-family: "Ubuntu", sans-serif; font-weight: 700;
    font-size: 60px; line-height: 1; letter-spacing: -0.5px;
    color: var(--paper);
  }
  .front-tagline {
    position: absolute; left: 242px; top: 201px;
    font-family: "Open Sans", sans-serif; font-weight: 600;
    font-size: 18px; line-height: 1; letter-spacing: 0.6px;
    color: #dfe4ea;
  }

  /* Back */
  .card-back { top: 524px; height: 358px; background: var(--paper); }
  .back-mark {
    position: absolute; left: 26px; top: 44px;
    width: 62px; height: 62px; border-radius: 50%;
    background: var(--blue);
  }
  .back-name {
    position: absolute; left: 134px; top: 50px;
    font-family: "Ubuntu", sans-serif; font-weight: 700;
    font-size: 44px; line-height: 1; letter-spacing: -0.4px;
    color: var(--navy);
  }
  .back-tagline {
    position: absolute; left: 134px; top: 91px;
    font-family: "Open Sans", sans-serif; font-weight: 600;
    font-size: 13.5px; line-height: 1; letter-spacing: 0.4px;
    color: var(--ink-soft);
  }
  .back-watermark {
    position: absolute; left: 288px; top: 88px;
    width: 310px; height: 250px; border-radius: 48% 52% 40% 44%;
    background: linear-gradient(120deg, #d6dcf3 0%, #e2f1fb 45%, #eceeef 100%);
    opacity: 0.85;
  }
  .divider {
    position: absolute; left: 11px; top: 226px;
    width: 606px; height: 3px; background: var(--bright);
  }
  .holder {
    position: absolute; right: 31px; top: 192px; text-align: right;
  }
  .holder-name {
    font-family: "Open Sans", sans-serif; font-size: 25px; line-height: 1;
    color: #5a5e63; letter-spacing: -0.5px;
  }
  .holder-name b { font-weight: 700; }
  .holder-role {
    display: inline-block; margin-top: 2px; padding: 0 6px;
    background: var(--paper);
    font-family: "Open Sans", sans-serif; font-weight: 700;
    font-size: 15.5px; line-height: 20px; letter-spacing: 1px;
    color: var(--bright); position: relative; z-index: 1;
  }
  .contacts {
    position: absolute; left: 25px; top: 252px; list-style: none;
    font-family: "Open Sans", sans-serif; font-weight: 700;
    font-size: 16px; color: var(--ink);
  }
  .contacts li { display: flex; align-items: center; height: 22px; }
  .contacts svg { width: 16px; height: 16px; margin-right: 7px; flex: none; }
  .footer-bands { position: absolute; left: 0; bottom: 0; width: 628px; height: 21px; }
</style>
</head>
<body>
<main class="stage">

  <section class="card card-front" aria-label="Card front">
    <div class="front-mark"></div>
    <div class="front-name">corvanth</div>
    <div class="front-tagline">CLARITY FOR GROWING FIRMS</div>
  </section>

  <section class="card card-back" aria-label="Card back">
    <div class="back-watermark" role="img" aria-label="Faint brand decoration area"></div>
    <div class="back-mark"></div>
    <div class="back-name">corvanth</div>
    <div class="back-tagline">CLARITY FOR GROWING FIRMS</div>

    <div class="divider"></div>
    <div class="holder">
      <div class="holder-name"><b>Tomás</b>Ferreira</div>
      <div class="holder-role">PARTNER</div>
    </div>

    <ul class="contacts">
      <li>
        <svg viewBox="0 0 16 16" aria-hidden="true"><rect x="4" y="1" width="8" height="14" rx="1.5" fill="var(--bright)"/><rect x="5.5" y="3" width="5" height="8" fill="#fff"/><circle cx="8" cy="13" r="0.9" fill="#fff"/></svg>
        +351 912 480 735
      </li>
      <li>
        <svg viewBox="0 0 16 16" aria-hidden="true"><rect x="0.5" y="3" width="15" height="10" fill="var(--bright)"/><path d="M0.5 3 L8 9 L15.5 3 M0.5 13 L6 8 M15.5 13 L10 8" stroke="#fff" stroke-width="1.2" fill="none"/></svg>
        tomas.ferreira@corvanth.com
      </li>
      <li>
        <svg viewBox="0 0 16 16" aria-hidden="true"><circle cx="8" cy="8" r="7.2" fill="var(--bright)"/><path d="M1 8 H15 M8 1 V15 M3 4.5 H13 M3 11.5 H13" stroke="#fff" stroke-width="0.9" fill="none"/><ellipse cx="8" cy="8" rx="3.2" ry="7" stroke="#fff" stroke-width="0.9" fill="none"/></svg>
        www.corvanth.com
      </li>
    </ul>

    <svg class="footer-bands" viewBox="0 0 628 21" aria-hidden="true">
      <polygon points="0,0 195,0 214,21 0,21" fill="var(--band-grey)"/>
      <polygon points="205,0 628,0 628,21 224,21" fill="var(--bright)"/>
      <polygon points="205,0 628,0 628,3 208,3" fill="#fff"/>
    </svg>
  </section>

</main>
</body>
</html>
```